Homepage für Unternehmensberatung
Zielgruppe
Wir sind eine Unternehmensberatung mit einem klaren Branchenfokus auf Banken / Finanzdienstleister.
Unsere Dienstleistungsprodukte lassen sich grob in folgende Themencluster unterteilen:
1)Strategieentwicklung
o IT-Strategie, IT-Architektur, IT-Bebauungsplan
2) Projektmanagement
o Projektportfoliomgmt., Programmmgmt., Projektmanagement, Projektcontrolling
3) Fachberatung
o Bankfachliche IT- Beratung mit Schwerpunkten Kredit, Wertpapiergeschäft,
Bankenaufsichtsrecht, Liquiditätsmanagement
o Anforderungsmanagement inkl. Aufbau von Bewertungs- und Priorisierungsmethoden
4) Prozessberatung/-optimierung
o Prozessanalyse, Prozessdesign, Prozessdokumentation
o Prozessoptimierung auf Basis etablierter Messmethoden
Unser Firmenname Morgenlichtwerk hat für uns eine Doppelbedeutung:
1. Im Außenverhältnis: Wir verstehen uns als Morgenlichtwerk unserer Kunden
2. Im Innenverhältnis: Wir pflegen einen partnerschaftlichen Umgang mit unseren
Mitarbeitern (Teamarbeit)
Aktuell sind wir ein kleines aber feines Team von erfahrenen und hochmotivierten Kollegen. Unsere Mitarbeiter sind ehemalige Führungskräfte sowie erfahrenen Unternehmensberater.
Aufgabenstellung
Entwurf / Design von 2 Seiten:
1. Seite / Startseite:
Simple und elegante Darstellung der oben genannten 4 Themencluster (z.B. Bild/Piktogramm, Textkasten) sowie einer Navigationsmöglichkeit zu folgenden Detailsichten:
• Unternehmen
• Beratungsangebot (siehe Themencluster)
• Partnerunternehmen
• Kontakt
2. Seite / 2. Ebene:
Entwurf einer Möglichkeit zur Erläuterung/Darstellung von Inhalten der Startseite.
Die Themencluster sollten auf jeder Ebene immer „anklickbar“/ zu sehen sein.
Logo
Das angehängte Logo ist in die Website einzubinden. Stil und Farben sollen übernommen werden bzw. sind Basis für das Design.
Lizenzen
Lizenz für eingesetzte Fotos und Illustrationen soll enthalten / Open-Source sein. Wenn nicht dann bitte zusätzliche Kosten angeben.

```html
<!DOCTYPE html>
<html lang="de">
<head>
<meta charset="utf-8">
<title>Morgenlichtwerk – Management- und Prozessberatung</title>
<link rel="stylesheet" href="https://fonts.googleapis.com/css2?family=Open+Sans:wght@400;600;700&family=Roboto+Condensed:wght@300;400&family=Ubuntu:wght@300;400&display=swap">
<style>
  :root{
    --brand-blue:#1a73ad;
    --accent-blue:#4a9ad2;
    --text-grey:#555c62;
    --heading-grey:#4b565e;
    --caption-blue:#2d5f86;
    --button-grey:#555555;
    --footer-bg:#3b3b3b;
    --footer-text:#9a9a9a;
    --social-bg:#6a6a6a;
    --badge-grey:#8a8f93;
    --white:#ffffff;
  }
  *{box-sizing:border-box;margin:0;padding:0}
  html,body{width:864px;height:1200px;overflow:hidden;background:var(--white)}
  body{font-family:"Open Sans",sans-serif;color:var(--text-grey);position:relative}

  .site-header{position:absolute;left:0;top:0;width:864px;height:87px;
    background:linear-gradient(90deg,#f4f5f6 0%,#ffffff 40%,#f0f1f2 85%,#dfe1e3 100%);
    border-bottom:1px solid var(--accent-blue)}
  .brand{position:absolute;left:125px;top:25px;display:flex;align-items:center;gap:8px}
  .brand-dot{width:40px;height:40px;border-radius:50%;background:var(--brand-blue)}
  .brand-name{font-size:17px;font-weight:400;color:var(--brand-blue);letter-spacing:.2px}
  .main-nav{position:absolute;right:123px;top:38px;display:flex;gap:7px;font-size:10px;font-weight:600}
  .main-nav a{color:var(--brand-blue);text-decoration:none}
  .main-nav a.current{color:#3a3f44}

  .hero{position:absolute;left:0;top:87px;width:864px;height:402px;
    background:
      radial-gradient(ellipse 30% 60% at 24% 45%,rgba(215,230,242,.9) 0%,rgba(215,230,242,0) 100%),
      radial-gradient(ellipse 45% 55% at 62% 35%,rgba(236,243,245,.85) 0%,rgba(236,243,245,0) 100%),
      linear-gradient(180deg,rgba(0,0,0,0) 60%,rgba(70,90,100,.35) 100%),
      linear-gradient(90deg,#8ea9b3 0%,#c3d7de 25%,#d8e6ea 55%,#c5d6dc 80%,#a4b9c0 100%)}
  .slider-arrow{position:absolute;top:196px;width:26px;height:26px;border-radius:50%;background:#3a3a3a}
  .slider-arrow.prev{left:10px}
  .slider-arrow.next{left:827px}
  .slider-arrow svg{position:absolute;left:7px;top:7px}
  .hero-title{position:absolute;left:350px;top:136px;width:380px;text-align:center;line-height:1}
  .hero-title .kicker{display:block;font-size:17px;font-weight:600;color:#5a646b;margin-left:60px}
  .hero-title .main{display:block;font-size:31px;font-weight:700;color:var(--brand-blue);margin-top:-2px}
  .hero-title .sub{display:block;font-size:18px;font-weight:700;color:var(--white);margin-top:-3px}
  .hero-copy{position:absolute;left:462px;top:234px;width:230px;text-align:right;
    font-family:"Roboto Condensed",sans-serif;font-weight:400;font-size:9.2px;line-height:12.4px;color:var(--white)}

  .services{position:absolute;left:0;top:520px;width:864px}
  .service{position:absolute;width:142px;text-align:center}
  .service-icon{width:40px;height:40px;border-radius:50%;background:var(--accent-blue);margin:0 auto;display:flex;align-items:center;justify-content:center}
  .service h2{margin-top:20px;font-size:11.5px;font-weight:600;color:var(--heading-grey);white-space:nowrap;letter-spacing:.1px}
  .service p{margin-top:12px;font-size:9.4px;line-height:15.7px}

  .cta{position:absolute;left:126px;top:750px;width:613px;height:61px;background:var(--accent-blue);border:1px solid #3b86bd}
  .cta-lead{position:absolute;left:13px;top:16px;font-size:12.4px;color:var(--white)}
  .cta-note{position:absolute;left:13px;top:36px;font-size:9.4px;color:#1f3142}
  .cta-button{position:absolute;left:410px;top:12px;width:184px;height:35px;background:var(--button-grey);border:1px solid #3e3e3e;
    color:var(--white);font-size:12.4px;display:flex;align-items:center;justify-content:center}

  .teasers{position:absolute;left:125px;top:850px}
  .teaser{position:absolute;top:0;width:144px}
  .teaser-media{position:relative;width:144px;height:101px}
  .teaser-badge{position:absolute;right:0;top:0;width:14px;height:14px;background:var(--badge-grey)}
  .teaser-badge svg{position:absolute;left:3px;top:3px}
  .teaser p{margin-top:30px;font-family:"Ubuntu",sans-serif;font-weight:300;font-size:7.8px;line-height:14.4px;color:var(--caption-blue);width:142px}

  .site-footer{position:absolute;left:0;top:1055px;width:864px;height:145px;background:var(--footer-bg)}
  .footer-text{position:absolute;top:46px;font-family:"Ubuntu",sans-serif;font-weight:300;font-size:7.8px;line-height:14.4px;color:var(--footer-text)}
  .footer-text.about{left:125px;width:210px}
  .footer-text.newsletter{left:542px;width:190px}
  .social{position:absolute;left:353px;top:36px;width:141px;height:41px;background:#353535;display:flex;gap:7px;padding:8px 0 0 14px}
  .social span{width:25px;height:25px;background:var(--social-bg)}
  .email-field{position:absolute;left:542px;top:81px;width:160px;height:23px;background:var(--white);
    font-family:"Ubuntu",sans-serif;font-size:7.8px;color:#777;padding:7px 10px}
</style>
</head>
<body>
  <header class="site-header">
    <div class="brand"><span class="brand-dot"></span><span class="brand-name">Morgenlichtwerk</span></div>
    <nav class="main-nav">
      <a class="current" href="#">HOME</a>
      <a href="#">UNTERNEHMEN</a>
      <a href="#">BERATUNGSANGEBOT</a>
      <a href="#">PARTNERUNTERNEHMEN</a>
      <a href="#">KONTAKT</a>
    </nav>
  </header>

  <section class="hero" role="img" aria-label="Bühnenfoto: unscharfe Bürostadt in Blaugrau mit lächelndem Berater im hellblauen Hemd">
    <span class="slider-arrow prev"><svg width="12" height="12" viewBox="0 0 12 12"><path d="M8 1 3 6l5 5" fill="none" stroke="#fff" stroke-width="2"/></svg></span>
    <span class="slider-arrow next"><svg width="12" height="12" viewBox="0 0 12 12"><path d="M4 1l5 5-5 5" fill="none" stroke="#fff" stroke-width="2"/></svg></span>
    <h1 class="hero-title">
      <span class="kicker">EFFIZIENZSTEIGERNDE</span>
      <span class="main">BERATUNG</span>
      <span class="sub">FÜR BANKEN &amp; FINANZDIENSTLEISTER</span>
    </h1>
    <p class="hero-copy">Lorem ipsum dolor sit amet, consectetur adipiscing elit. Nam laoreet dignissim sapien. Praesent non turpis est. Sed mattis ante at egestas vehicula. Suspendisse a eros eu massa elementum placerat non sed purus. Etiam tincidunt aliquam iaculis. Curabitur mi metus, semper at felis ac, vulputate consequat velit.</p>
  </section>

  <section class="services">
    <article class="service" style="left:125px">
      <div class="service-icon"><svg width="18" height="16" viewBox="0 0 18 16"><path d="M2 15V9M6 15V6M10 15V8M14 15V3" stroke="#fff" stroke-width="2.4"/><path d="M1 8l5-4 4 3 6-6" fill="none" stroke="#fff" stroke-width="1.4"/></svg></div>
      <h2>STRATEGIEENTWICKLUNG</h2>
      <p>Bacon ipsum dolor sit amet doner meatball jowl short ribs, chicken prosciutto salami frank-furter. Pig drumstick turducken short ribs, brisket meatloaf ham hock shankle andouille corned beef strip steak.</p>
    </article>
    <article class="service" style="left:287px">
      <div class="service-icon"><svg width="20" height="15" viewBox="0 0 20 15"><ellipse cx="8" cy="6" rx="7" ry="5" fill="#fff"/><ellipse cx="13" cy="9" rx="6" ry="4.2" fill="#fff" stroke="#4a9ad2" stroke-width="1.2"/></svg></div>
      <h2>PROJEKTMANAGEMENT</h2>
      <p>Bacon ipsum dolor sit amet doner meatball jowl short ribs, chicken prosciutto salami frank-furter. Pig drumstick turducken short ribs, brisket meatloaf ham hock shankle andouille corned beef strip steak.</p>
    </article>
    <article class="service" style="left:438px">
      <div class="service-icon"><svg width="18" height="18" viewBox="0 0 18 18"><path d="M3 3l12 12M15 3 3 15" stroke="#fff" stroke-width="3.2"/></svg></div>
      <h2>FACHBERATUNG</h2>
      <p>Bacon ipsum dolor sit amet doner meatball jowl short ribs, chicken prosciutto salami frankfurter. Pig drumstick tur-ducken short ribs, brisket mea-tloaf ham hock shankle and-ouille corned beef strip steak.</p>
    </article>
    <article class="service" style="left:596px">
      <div class="service-icon"><svg width="18" height="18" viewBox="0 0 18 18"><path d="M3 3l12 12M15 3 3 15" stroke="#fff" stroke-width="3.2"/></svg></div>
      <h2>PROZESSOPTIMIERUNG</h2>
      <p>Bacon ipsum dolor sit amet doner meatball jowl short ribs, chicken prosciutto salami frankfurter. Pig drumstick tur-ducken short ribs, brisket mea-tloaf ham hock shankle and-ouille corned beef strip steak.</p>
    </article>
  </section>

  <aside class="cta">
    <p class="cta-lead">Ja, ich möchte mehr erfahren über die Beratungsprodukte.</p>
    <p class="cta-note">Bitte vereinbaren Sie einen unverbindlichen Termin.</p>
    <a class="cta-button">mehr erfahren</a>
  </aside>

  <section class="teasers">
    <article class="teaser" style="left:0">
      <div class="teaser-media" role="img" aria-label="Illustration eines blauen Ringdiagramms mit Serviceplattform" style="background:radial-gradient(ellipse 60% 55% at 50% 50%,#3f8fcb 0%,#8cc0e4 55%,#ffffff 100%)"><span class="teaser-badge"><svg width="8" height="8" viewBox="0 0 8 8"><path d="M1.5 .5h3.5l1.5 1.5v5.5h-5z" fill="none" stroke="#fff"/></svg></span></div>
      <p>Donec dictum libero vel orci malesuada mattis. Suspendisse libero ante, varius ac laoreet vel, blandit</p>
    </article>
    <article class="teaser" style="left:156px">
      <div class="teaser-media" role="img" aria-label="Foto eines jungen Mannes im blau gestreiften Hemd" style="background:linear-gradient(180deg,#f0ede8 0%,#d8c2ae 45%,#6f93bd 80%,#4f7fb3 100%)"><span class="teaser-badge"><svg width="8" height="8" viewBox="0 0 8 8"><path d="M2 1l5 3-5 3z" fill="#fff"/></svg></span></div>
      <p>Lorem ipsum dolor sit amet, consectetur adipiscing elit. Sed blandit massa vel mauris sollicitudin dignissim.</p>
    </article>
    <article class="teaser" style="left:313px">
      <div class="teaser-media" role="img" aria-label="Foto einer lächelnden Frau am Schreibtisch mit Unterlagen" style="background:linear-gradient(180deg,#f2f2f2 0%,#e2d6ce 50%,#a39894 100%)"><span class="teaser-badge"><svg width="8" height="8" viewBox="0 0 8 8"><rect x=".5" y="1.5" width="7" height="5" fill="none" stroke="#fff"/><path d="M1 6l2-2 2 2" fill="none" stroke="#fff"/></svg></span></div>
      <p>Aenean convallis aliquet lacus vitae tempus. Suspendisse accumsan nisl sit amet justo auctor id accumsan</p>
    </article>
    <article class="teaser" style="left:470px">
      <div class="teaser-media" role="img" aria-label="Foto eines älteren Geschäftsmannes im hellen Anzug im Büro" style="background:linear-gradient(90deg,#dfe3e6 0%,#cfcac3 55%,#e8e7e4 100%)"><span class="teaser-badge"><svg width="8" height="8" viewBox="0 0 8 8"><path d="M1 7l6-6M2.5 3.5l-1 1M5.5 4.5l1-1" stroke="#fff" stroke-width="1.2"/></svg></span></div>
      <p>Susce ac dolor in erat elementum auctor ante. puspendisse nibh leo, hendrerit quis sed dictum</p>
    </article>
  </section>

  <footer class="site-footer">
    <p class="footer-text about">Integer eu libero sit amet nisl vestibulum semper. Fusce nec porttitor massa. In nec neque elit. Curabitur malesuada ligula vitae purus ornare onec etea magna diam varius.</p>
    <div class="social" aria-label="Soziale Netzwerke"><span></span><span></span><span></span><span></span></div>
    <p class="footer-text newsletter">Integer eu libero sit amet nisl vestibulum semp edfs pdisioolpr.</p>
    <div class="email-field">Your Email...</div>
  </footer>
</body>
</html>
```